Tallow Crest Business Card

We need a business card designed for a a company called "Tallow Crest". We offer consulting, coaching and training to business leaders and coaches (across the world) using the latest findings in neuroscience, social and emotional intelligence and positive psychology. The final design should communicate the use of brain science to create sustainable relationships.

The card should be doublesided. The logo is attached and names and titles will be provided to the successful designer. Thank you.

Industry/Entity Type

Training

```html
<!DOCTYPE html>
<html lang="en">
<head>
<meta charset="UTF-8">
<title>Tallow Crest Business Card</title>
<link href="https://fonts.googleapis.com/css2?family=Lato:ital,wght@0,400;0,700;1,400&display=swap" rel="stylesheet">
<style>
  :root {
    --brand-blue: #1a9ad6;
    --brand-green: #b8d433;
    --card-white: #ffffff;
    --card-dark: #3a3838;
    --ink: #2b2b2b;
    --backdrop: #e4e9ec;
  }
  * { box-sizing: border-box; margin: 0; padding: 0; }
  html, body {
    width: 1200px; height: 960px; overflow: hidden;
    background: var(--backdrop);
    font-family: 'Lato', sans-serif;
  }
  .canvas {
    position: relative; width: 1200px; height: 960px;
  }
  .card {
    position: absolute; left: 250px; width: 700px; height: 400px;
    overflow: hidden;
    box-shadow: 0 6px 18px rgba(0,0,0,0.12);
  }
  .card-front { top: 50px; background: var(--card-white); }
  .card-back { top: 510px; background: var(--card-dark); }

  .colour-band {
    position: absolute; left: 0; right: 0; bottom: 0; height: 26px;
    display: flex;
  }
  .colour-band .band-blue { width: 47%; background: var(--brand-blue); }
  .colour-band .band-green { flex: 1; background: var(--brand-green); }

  .holder { position: absolute; left: 54px; top: 72px; }
  .holder-name {
    font-size: 31px; font-weight: 400; letter-spacing: 0.5px;
    color: var(--ink); text-transform: uppercase;
    padding-bottom: 4px;
    border-bottom: 2px solid var(--brand-blue);
    display: inline-block;
  }
  .holder-title {
    margin-top: 10px; font-size: 20px; font-style: italic; color: var(--ink);
  }

  .front-brand {
    position: absolute; right: 40px; top: 150px; width: 270px; text-align: center;
  }
  .brand-name {
    font-family: 'Lato', sans-serif; font-weight: 700;
    color: var(--brand-blue); white-space: nowrap;
  }
  .front-brand .brand-name { font-size: 36px; }
  .brand-tagline {
    margin-top: 8px; font-size: 17px; color: var(--brand-blue); white-space: nowrap;
  }

  .contact-list {
    position: absolute; left: 54px; bottom: 62px; list-style: none;
  }
  .contact-list li {
    display: flex; align-items: center; gap: 14px;
    font-size: 19px; color: var(--ink); line-height: 28px;
  }
  .contact-list svg { width: 20px; height: 20px; flex: none; }
  .contact-web { font-weight: 700; }
  .contact-web .accent { color: var(--brand-blue); }

  .back-brand {
    position: absolute; left: 0; right: 0; top: 130px; text-align: center;
  }
  .back-brand .brand-name { font-size: 60px; }
  .back-web {
    margin-top: 16px; font-size: 18px; letter-spacing: 3px; color: var(--brand-blue);
  }
</style>
</head>
<body>
<main class="canvas">

  <section class="card card-front" aria-label="Card front">
    <div class="holder">
      <h1 class="holder-name">Harriet Lomax</h1>
      <p class="holder-title">Director</p>
    </div>

    <div class="front-brand">
      <p class="brand-name">Tallow Crest</p>
      <p class="brand-tagline">insight for people who lead</p>
    </div>

    <ul class="contact-list">
      <li>
        <svg viewBox="0 0 20 20" aria-hidden="true">
          <rect x="2" y="3" width="16" height="15" rx="2" fill="none" stroke="var(--brand-blue)" stroke-width="1.8"/>
          <rect x="5" y="6" width="4" height="9" fill="var(--brand-blue)"/>
          <circle cx="12.5" cy="8" r="1" fill="var(--brand-blue)"/>
          <circle cx="15" cy="8" r="1" fill="var(--brand-blue)"/>
          <circle cx="12.5" cy="11" r="1" fill="var(--brand-blue)"/>
          <circle cx="15" cy="11" r="1" fill="var(--brand-blue)"/>
          <circle cx="12.5" cy="14" r="1" fill="var(--brand-blue)"/>
          <circle cx="15" cy="14" r="1" fill="var(--brand-blue)"/>
        </svg>
        <span>+61 400 555 019</span>
      </li>
      <li>
        <svg viewBox="0 0 20 20" aria-hidden="true">
          <rect x="2" y="4" width="16" height="12" fill="none" stroke="var(--brand-blue)" stroke-width="1.8"/>
          <path d="M2 4 L10 11 L18 4 M2 16 L8 10 M18 16 L12 10" fill="none" stroke="var(--brand-blue)" stroke-width="1.5"/>
        </svg>
        <span>harriet@tallowcrest.com</span>
      </li>
      <li class="contact-web">
        <svg viewBox="0 0 20 20" aria-hidden="true">
          <path d="M10 2 L19 10 L16.5 10 L16.5 18 L12 18 L12 13 L8 13 L8 18 L3.5 18 L3.5 10 L1 10 Z" fill="var(--brand-blue)"/>
        </svg>
        <span>www.<span class="accent">tallowcrest</span>.com</span>
      </li>
    </ul>

    <div class="colour-band"><span class="band-blue"></span><span class="band-green"></span></div>
  </section>

  <section class="card card-back" aria-label="Card back">
    <div class="back-brand">
      <p class="brand-name">Tallow Crest</p>
      <p class="back-web">www.tallowcrest.com</p>
    </div>
    <div class="colour-band"><span class="band-blue"></span><span class="band-green"></span></div>
  </section>

</main>
</body>
</html>
```